Redesign of an educational Eye website for Medical Students and Healthcare professionals

www.corvellelearninghub.com is an educational resource, illustrated using high quality 3D animations, for undergraduate medical students and healthcare professionals to learn about the anatomy of the human eye and associated common eye disorders.

The website was originally developed (using a Joomla template) a couple of years ago and we now want to update the brand and design of the site. Example content and animations can be found at https://www.corvellelearninghub.com/overview or https://www.corvellelearninghub.com/ocular-anatomy/orbital-anatomy

We would like a new logo and home page design (to include new colour palette, fonts and updated overall design).

The attached PowerPoint contains an example layout of the revised components we want to appear on the new Home page. We plan to have a hero panel at the top of page playing a short video of some of the animations. Similar to how this site works (www.zeptal.uk.com).

We want the new site to feel Professional, Modern and Clean and simple.

Target Market(s)

Undergraduate medical students and Healthcare Professionals

Industry/Entity Type

Medical

Logo Text

Corvelle Learning Hub

Number of Pages Required

1 page

Font styles to use
Sans Serif

Colors

Designer to choose colors to be used in the design.

```html
<!DOCTYPE html>
<html lang="en">
<head>
<meta charset="utf-8">
<title>Corvelle Learning Hub</title>
<link rel="stylesheet" href="https://fonts.googleapis.com/css2?family=Lato:wght@300;400;700&display=swap">
<style>
  :root{
    --sky:#03aef0;
    --navy:#0d3a8a;
    --ink:#3a3f47;
    --muted:#8a9099;
    --tile:#ebebeb;
    --shape:#9c9c9c;
    --white:#ffffff;
    --stage:#f4f5f7;
    --hero-a:#5d8cc2;
    --hero-b:#2766ab;
    --hero-c:#174f91;
  }
  *{box-sizing:border-box;margin:0;padding:0}
  html,body{width:1200px;height:1000px;overflow:hidden}
  body{background:var(--stage);font-family:"Lato",Arial,sans-serif;color:var(--ink);position:relative}
  .page{position:absolute;left:32px;top:27px;width:1136px;height:973px;background:var(--white);overflow:hidden}
  .topbar{height:43px;background:var(--sky);display:flex;align-items:center;padding-left:90px;gap:34px;color:var(--white);font-size:13px;font-weight:700}
  .topbar span{display:flex;align-items:center;gap:8px}
  .nav{height:85px;display:flex;align-items:center;padding:0 88px 0 90px;position:relative}
  .brand{display:flex;align-items:center;gap:8px;color:var(--navy);font-weight:700;font-size:17px;width:201px}
  .brand-dot{width:16px;height:16px;border-radius:50%;background:var(--sky)}
  .menu{display:flex;gap:24px;font-size:15px;color:var(--ink)}
  .account{margin-left:auto;display:flex;align-items:center;gap:24px;font-size:15px;color:var(--ink)}
  .hero{position:relative;height:511px}
  .hero-media{position:absolute;inset:0;background:radial-gradient(ellipse at 35% 40%,var(--hero-a),transparent 60%),linear-gradient(100deg,var(--hero-b),var(--hero-c))}
  .hero-copy{position:absolute;left:96px;top:150px;color:var(--white)}
  .hero-copy h1{font-size:41px;font-weight:400;letter-spacing:.2px}
  .hero-copy p{margin-top:22px;width:550px;font-size:14px;line-height:17px;font-weight:400}
  .cta{margin-top:36px;display:flex;gap:11px}
  .btn{width:226px;height:47px;display:flex;align-items:center;justify-content:center;font-size:10.5px;color:var(--white)}
  .btn-primary{background:var(--sky)}
  .btn-outline{border:1.5px solid var(--white)}
  .play{position:absolute;left:998px;top:229px}
  .partners h2{text-align:center;margin-top:82px;font-size:28px;font-weight:300;color:var(--ink)}
  .partners h2 strong{color:var(--navy);font-weight:400}
  .grid{position:absolute;left:151px;top:808px;display:grid;grid-template-columns:repeat(6,124px);column-gap:18px;row-gap:13px}
  .tile{height:90px;background:var(--tile);display:flex;align-items:center;justify-content:center}
  .tile i{display:block;background:var(--shape)}
  .sq{width:70px;height:22px}
  .ci{width:40px;height:40px;border-radius:50%}
  .arrow{position:absolute;top:890px;font-size:20px;color:var(--ink)}
</style>
</head>
<body>
<div class="page">
  <div class="topbar">
    <span><svg width="15" height="11" viewBox="0 0 15 11" fill="none" stroke="#fff" stroke-width="1.2"><rect x=".6" y=".6" width="13.8" height="9.8"/><path d="M.6.6 7.5 6l6.9-5.4"/></svg>info@corvellelearninghub.com</span>
    <span><svg width="13" height="13" viewBox="0 0 13 13"><path fill="#fff" d="M3 1l2 2.5-1.2 1.4a7 7 0 0 0 4.3 4.3L9.5 8 12 10l-1.5 2A10 10 0 0 1 1 2.5z"/></svg>+1 (555) 0142 386</span>
  </div>
  <header class="nav">
    <div class="brand"><span class="brand-dot"></span>Corvelle Learning Hub</div>
    <nav class="menu"><span>Home</span><span>About</span><span>Services</span><span>Portfolio</span><span>Contact</span></nav>
    <div class="account"><span>Sign in</span><span>Sign up</span>
      <svg width="19" height="19" viewBox="0 0 19 19" fill="none" stroke="#a8adb4" stroke-width="1.4"><circle cx="8" cy="8" r="6.5"/><path d="M13 13l5 5"/></svg>
    </div>
  </header>
  <section class="hero">
    <div class="hero-media" role="img" aria-label="Blurred hospital corridor with medical staff in motion, tinted blue"></div>
    <div class="hero-copy">
      <h1>Learn Faster and Smarter</h1>
      <p>Corvelle Learning Hub helps undergraduates and healthcare professionals to learn or update their knowledge about the clinically relevant anatomy, ophthalmic examination techniques and common eye disorders of the human eye.</p>
      <div class="cta">
        <span class="btn btn-primary">Undergraduates “Learn More”</span>
        <span class="btn btn-outline">Healthcare Professinals “Learn More”</span>
      </div>
    </div>
    <svg class="play" width="50" height="50" viewBox="0 0 50 50" fill="none" stroke="#fff" stroke-opacity=".85" stroke-width="1.5"><circle cx="25" cy="25" r="24"/><path d="M20 15v20l15-10z"/></svg>
  </section>
  <section class="partners">
    <h2>Trusted <strong>Across The World</strong></h2>
    <span class="arrow" style="left:88px">&lt;</span>
    <span class="arrow" style="left:1034px">&gt;</span>
    <div class="grid">
      <div class="tile"><i class="sq"></i></div><div class="tile"><i class="sq"></i></div><div class="tile"><i class="ci"></i></div>
      <div class="tile"><i class="sq"></i></div><div class="tile"><i class="ci"></i></div><div class="tile"><i class="sq"></i></div>
      <div class="tile"><i class="sq"></i></div><div class="tile"><i class="sq"></i></div><div class="tile"><i class="ci"></i></div>
      <div class="tile"><i class="sq"></i></div><div class="tile"><i class="ci"></i></div><div class="tile"><i class="sq"></i></div>
    </div>
  </section>
</div>
</body>
</html>
```